Food company needs package designed to hold recipe cards.

We are a food manufacturer in Texas and we need a design for a small package that will hold 50 recipe cards. The end-product will be sold at retail stores across the USA. The package will be made from 24 pt cardstock. When package box is constructed and glued together, the measurements will be 5.25” x 0.9” x 4.25”.
We would like to see an eye-catching ARTISTIC design. The design does not necessarily need to include images of food to convey the message that recipes are included inside the box. However, if images of food are not included, text / copy will be needed to give details of the contents.
Target Market(s)
Cooks, Foodies, Chefs, Shoppers.
Industry/Entity Type
Food Manufacturer.
Requirements
Must have
- One or more of our logos. Contents included in the box; "Recipe Cards".
Should not have
- Bee graphics, honey dipper graphics. This project is about food, not bees or honey.

```html
<!DOCTYPE html>
<html lang="en">
<head>
<meta charset="utf-8">
<title>Recipe Cards – Box Lid</title>
<link rel="stylesheet" href="https://fonts.googleapis.com/css2?family=Sorts+Mill+Goudy&display=swap">
<style>
  :root {
    --stage: #f1f2f3;
    --teal: #2f5f73;
    --teal-light: #3a6d82;
    --ink-dark: #17394a;
    --line-blue: #8cc4d4;
    --copper: #eaa88c;
    --copper-light: #f6cdb9;
    --gold: #c9a448;
    --white: #ffffff;
  }
  * { margin: 0; padding: 0; box-sizing: border-box; }
  html, body { width: 1200px; height: 675px; overflow: hidden; background: var(--stage); }
  body { font-family: "Sorts Mill Goudy", Georgia, serif; }

  .lid {
    position: absolute; left: 250px; top: 55px; width: 700px; height: 566px;
    background: radial-gradient(circle at 61% 30%, var(--teal-light) 0%, var(--teal) 60%);
    color: var(--white);
  }
  .ornament {
    position: absolute; left: 300px; top: 30px; width: 270px; height: 220px;
    background: radial-gradient(ellipse at center, var(--ink-dark) 0%, rgba(23,57,74,0.75) 55%, rgba(23,57,74,0) 72%);
  }
  .seal {
    position: absolute; left: 365px; top: 70px; width: 140px; height: 140px; border-radius: 50%;
    background: radial-gradient(circle at 40% 35%, var(--copper-light), var(--copper));
    border: 5px solid var(--white);
    display: flex; align-items: center; justify-content: center; text-align: center;
  }
  .seal-name { font-size: 17px; line-height: 1.15; color: var(--white); letter-spacing: 1px; text-transform: uppercase; padding: 0 14px; }

  .rule { position: absolute; height: 2px; background: var(--line-blue); }
  .rule-top { left: 70px; top: 232px; width: 270px; }
  .rule-est { left: 530px; top: 232px; width: 110px; }
  .rule-mid { left: 70px; top: 322px; width: 570px; }
  .rule-low { left: 70px; top: 382px; width: 570px; }

  .origin-mark { position: absolute; left: 78px; top: 208px; width: 12px; height: 12px; background: var(--line-blue); }
  .origin { position: absolute; left: 104px; top: 200px; font-size: 12px; line-height: 1.05; letter-spacing: 2px; text-transform: uppercase; text-align: center; }

  .est { position: absolute; left: 580px; top: 190px; font-size: 13px; line-height: 1.05; letter-spacing: 2px; text-align: center; text-transform: uppercase; color: var(--line-blue); }
  .est .year { display: block; font-size: 20px; letter-spacing: 1px; color: var(--white); }

  .title { position: absolute; left: 66px; top: 240px; font-size: 74px; font-weight: 400; line-height: 1; letter-spacing: 1px; text-transform: uppercase; white-space: nowrap; }

  .count { position: absolute; left: 74px; top: 334px; line-height: 1.2; white-space: nowrap; }
  .count-num { font-size: 30px; color: var(--white); }
  .count-label { font-size: 14px; letter-spacing: 4px; text-transform: uppercase; color: var(--line-blue); margin-left: 6px; }

  .flourish { position: absolute; left: 100px; top: 396px; width: 190px; height: 44px;
    background: radial-gradient(ellipse at center, var(--ink-dark) 0%, rgba(23,57,74,0) 70%); }

  .brand { position: absolute; left: 70px; top: 458px; padding: 8px 4px; border-top: 2px solid var(--gold); border-bottom: 2px solid var(--gold); }
  .brand-name { display: block; font-size: 28px; line-height: 1.2; letter-spacing: 1px; text-transform: uppercase; color: var(--white); white-space: nowrap; }

  .web { position: absolute; right: 40px; bottom: 20px; font-size: 13px; line-height: 1.2; letter-spacing: 3px; text-transform: uppercase; color: var(--white); }
</style>
</head>
<body>
  <main class="lid">
    <div class="ornament" role="img" aria-label="Dark teal scrolling filigree ornament framing the seal"></div>
    <div class="seal"><span class="seal-name">Pecan Ridge Foods Co</span></div>

    <span class="origin-mark"></span>
    <p class="origin">Made in<br>Texas</p>
    <span class="rule rule-top"></span>

    <p class="est"><span class="year">2022</span>Est.</p>
    <span class="rule rule-est"></span>

    <h1 class="title">Recipe Cards</h1>
    <span class="rule rule-mid"></span>

    <p class="count"><span class="count-num">50</span><span class="count-label">Different Recipes</span></p>
    <span class="rule rule-low"></span>

    <div class="flourish" role="img" aria-label="Small dark teal decorative flourish"></div>

    <div class="brand"><span class="brand-name">Pecan Ridge Foods Co</span></div>
    <p class="web">www.pecanridgefoods.com</p>
  </main>
</body>
</html>
```